Meridale Dental Business Card

Please design a professional but colorful looking business card. Our new logo is attached. The card also needs the following information:
For ALL Your Dental Needs
Curtis L. Hobbel, D.D.S.
918-555-0147
20463-C North Fernwick, Bixby, OK 74031
www.meridaledentalok.example

Industry/Entity Type

Business

Colors

Designer to choose colors to be used in the design.

```html
<!DOCTYPE html>
<html lang="en">
<head>
<meta charset="utf-8">
<title>Meridale Dental – Business Card</title>
<link rel="stylesheet" href="https://fonts.googleapis.com/css2?family=Arimo:wght@400;700&family=Noto+Serif:ital@1&display=swap">
<style>
  :root {
    --page-bg: #e9e6e3;
    --card-bg: #ffffff;
    --ink-dark: #3a4246;
    --ink-grey: #8a8a8a;
    --ink-serif: #444444;
    --brand-blue: #1f63b4;
    --divider: #ececec;
    --faint-blue: #f1f4f9;
  }
  * { box-sizing: border-box; margin: 0; padding: 0; }
  html, body {
    width: 1200px;
    height: 1000px;
    overflow: hidden;
    background: var(--page-bg);
  }
  .business-card {
    position: absolute;
    left: 160px;
    top: 248px;
    width: 881px;
    height: 504px;
    background: var(--card-bg);
    overflow: hidden;
    box-shadow: 0 2px 10px rgba(0,0,0,0.12);
  }
  .brand-block {
    position: absolute;
    left: 40px;
    top: 46px;
    width: 258px;
    height: 404px;
    display: flex;
    flex-direction: column;
    align-items: center;
    justify-content: center;
    gap: 28px;
  }
  .brand-square {
    width: 150px;
    height: 150px;
    border-radius: 14px;
    background: var(--brand-blue);
  }
  .brand-name {
    font-family: "Arimo", Arial, sans-serif;
    font-weight: 700;
    font-size: 31px;
    color: var(--ink-dark);
    white-space: nowrap;
  }
  .divider {
    position: absolute;
    left: 328px;
    top: 46px;
    width: 1px;
    height: 400px;
    background: var(--divider);
  }
  .faint-mark {
    position: absolute;
    z-index: 0;
    left: 650px;
    top: 372px;
    width: 260px;
    height: 170px;
    border-radius: 26px;
    background: var(--faint-blue);
    filter: blur(8px);
    opacity: 0.85;
  }
  .contact-block {
    position: absolute;
    z-index: 1;
    left: 352px;
    top: 126px;
  }
  .slogan {
    font-family: "Noto Serif", Georgia, serif;
    font-style: italic;
    font-size: 36px;
    color: var(--ink-serif);
    line-height: 48px;
    margin-bottom: 2px;
    white-space: nowrap;
  }
  .contact-line {
    font-family: "Arimo", Arial, sans-serif;
    font-size: 26px;
    color: var(--ink-grey);
    line-height: 34.5px;
    white-space: nowrap;
  }
</style>
</head>
<body>
  <div class="business-card">
    <div class="faint-mark" aria-hidden="true"></div>
    <div class="brand-block">
      <div class="brand-square" aria-hidden="true"></div>
      <div class="brand-name">Meridale Dental</div>
    </div>
    <div class="divider" aria-hidden="true"></div>
    <div class="contact-block">
      <p class="slogan">For ALL your dental needs</p>
      <p class="contact-line">Curtis L. Hobbel, D.D.S.</p>
      <p class="contact-line">918-555-0147</p>
      <p class="contact-line">20463-C North Fernwick,</p>
      <p class="contact-line">Bixby, OK 74031</p>
      <p class="contact-line">www.meridaledentalok.example</p>
    </div>
  </div>
</body>
</html>
```